Single-sided business card for restaurant bellamonte with new logo made on this site

Business card options with new logo including restaurant name, address, phone number and website. This business card is single-sided only and will be presented at the hostess desk for clients to take. I would like to see options based on a cream card background, a white card background, a yellow card background and a burgundy colored background. It needs to be elegant and traditional.

Target Market(s)

local and international crowd

Industry/Entity Type

restaurant

Contact Information for Business Card

address, website and phone number

Font styles to use
Serif

Colors
EE7325
F08F49
F5BC92
FAE3D3
FDF4ED

Requirements
Must have
• new logo, address, phone number, website
Should not have
• more than three colors

```html
<!DOCTYPE html>
<html lang="es">
<head>
<meta charset="utf-8">
<title>Bellamonte – Tarjetas de presentación</title>
<link rel="stylesheet" href="https://fonts.googleapis.com/css2?family=Poppins:wght@600&display=swap">
<style>
  :root {
    --stage: #dcdcdc;
    --saffron: #e9aa2b;
    --gold: #e3ab2c;
    --burgundy: #4a1f1c;
    --paper-white: #f3f2ef;
    --paper-cream: #f4eecb;
    --ivory: #f4f2ee;
  }
  html, body {
    margin: 0;
    padding: 0;
    width: 799px;
    height: 1200px;
    overflow: hidden;
    background: var(--stage);
  }
  .stage {
    position: relative;
    width: 799px;
    height: 1200px;
  }
  .card {
    position: absolute;
    width: 281px;
    height: 490px;
    background: var(--bg);
    font-family: "Poppins", sans-serif;
    font-weight: 600;
    color: var(--ink);
    text-align: center;
  }
  .card--saffron  { left: 90px;  top: 73px;  --bg: var(--saffron);     --frame: var(--burgundy); --mark: var(--burgundy); --ink: var(--burgundy); --icon: var(--burgundy); }
  .card--burgundy { left: 432px; top: 73px;  --bg: var(--burgundy);    --frame: var(--ivory);    --mark: var(--ivory);    --ink: var(--ivory);    --icon: var(--gold); }
  .card--white    { left: 86px;  top: 618px; --bg: var(--paper-white); --frame: var(--gold);     --mark: var(--gold);     --ink: var(--burgundy); --icon: var(--gold); }
  .card--cream    { left: 428px; top: 618px; --bg: var(--paper-cream); --frame: var(--burgundy); --mark: var(--burgundy); --ink: var(--burgundy); --icon: var(--gold); }

  .card__frame {
    position: absolute;
    inset: 7px;
    border: 4px solid var(--frame);
  }
  .brand__square {
    position: absolute;
    left: 87px;
    top: 45px;
    width: 107px;
    height: 107px;
    background: var(--mark);
  }
  .brand__name {
    position: absolute;
    left: 0;
    right: 0;
    top: 176px;
    margin: 0;
    font-size: 25px;
    letter-spacing: 2.5px;
    color: var(--ink);
  }
  .contact__pin {
    position: absolute;
    left: 132px;
    top: 286px;
    width: 18px;
    height: 27px;
  }
  .contact__address {
    position: absolute;
    left: 0;
    right: 0;
    top: 320px;
    margin: 0;
    font-size: 13.5px;
    line-height: 16.5px;
    font-style: normal;
  }
  .contact__icons {
    position: absolute;
    left: 0;
    right: 0;
    top: 405px;
    display: flex;
    justify-content: center;
    gap: 4px;
  }
  .contact__icons svg { width: 16px; height: 16px; }
  .contact__lines {
    position: absolute;
    left: 0;
    right: 0;
    top: 427px;
    margin: 0;
    font-size: 11.5px;
    line-height: 16px;
    letter-spacing: 1px;
  }
</style>
</head>
<body>
<main class="stage">

  <section class="card card--saffron">
    <div class="card__frame"></div>
    <div class="brand__square"></div>
    <h1 class="brand__name">BELLAMONTE</h1>
    <svg class="contact__pin" viewBox="0 0 18 27" aria-hidden="true"><path d="M9 1a8 8 0 0 0-8 8c0 6 8 13 8 13s8-7 8-13a8 8 0 0 0-8-8z" fill="var(--icon)"/><circle cx="9" cy="8.5" r="3" fill="var(--bg)"/><rect x="2" y="24.5" width="14" height="2" fill="var(--icon)"/></svg>
    <address class="contact__address">Camelia 415<br>Playa Azul,<br>Guerrero CP 40880</address>
    <div class="contact__icons">
      <svg viewBox="0 0 16 16" aria-hidden="true"><circle cx="8" cy="8" r="8" fill="var(--icon)"/><path d="M5.2 4.2l1.4-.3.9 2-1 .8a5 5 0 0 0 2.7 2.7l.8-1 2 .9-.3 1.4c-3.6.5-7-2.9-6.5-6.5z" fill="var(--bg)"/></svg>
      <svg viewBox="0 0 16 16" aria-hidden="true"><circle cx="8" cy="8" r="8" fill="var(--icon)"/><g fill="none" stroke="var(--bg)" stroke-width="1"><circle cx="8" cy="8" r="4.8"/><ellipse cx="8" cy="8" rx="2" ry="4.8"/><path d="M3.2 8h9.6M8 3.2v9.6"/></g></svg>
    </div>
    <p class="contact__lines">744-312-0846<br>www.bellamonte.com.mx</p>
  </section>

  <section class="card card--burgundy">
    <div class="card__frame"></div>
    <div class="brand__square"></div>
    <h1 class="brand__name">BELLAMONTE</h1>
    <svg class="contact__pin" viewBox="0 0 18 27" aria-hidden="true"><path d="M9 1a8 8 0 0 0-8 8c0 6 8 13 8 13s8-7 8-13a8 8 0 0 0-8-8z" fill="var(--icon)"/><circle cx="9" cy="8.5" r="3" fill="var(--bg)"/><rect x="2" y="24.5" width="14" height="2" fill="var(--icon)"/></svg>
    <address class="contact__address">Camelia 415<br>Playa Azul,<br>Guerrero CP 40880</address>
    <div class="contact__icons">
      <svg viewBox="0 0 16 16" aria-hidden="true"><circle cx="8" cy="8" r="8" fill="var(--icon)"/><path d="M5.2 4.2l1.4-.3.9 2-1 .8a5 5 0 0 0 2.7 2.7l.8-1 2 .9-.3 1.4c-3.6.5-7-2.9-6.5-6.5z" fill="var(--bg)"/></svg>
      <svg viewBox="0 0 16 16" aria-hidden="true"><circle cx="8" cy="8" r="8" fill="var(--icon)"/><g fill="none" stroke="var(--bg)" stroke-width="1"><circle cx="8" cy="8" r="4.8"/><ellipse cx="8" cy="8" rx="2" ry="4.8"/><path d="M3.2 8h9.6M8 3.2v9.6"/></g></svg>
    </div>
    <p class="contact__lines">744-312-0846<br>www.bellamonte.com.mx</p>
  </section>

  <section class="card card--white">
    <div class="card__frame"></div>
    <div class="brand__square"></div>
    <h1 class="brand__name">BELLAMONTE</h1>
    <svg class="contact__pin" viewBox="0 0 18 27" aria-hidden="true"><path d="M9 1a8 8 0 0 0-8 8c0 6 8 13 8 13s8-7 8-13a8 8 0 0 0-8-8z" fill="var(--icon)"/><circle cx="9" cy="8.5" r="3" fill="var(--bg)"/><rect x="2" y="24.5" width="14" height="2" fill="var(--icon)"/></svg>
    <address class="contact__address">Camelia 415<br>Playa Azul,<br>Guerrero CP 40880</address>
    <div class="contact__icons">
      <svg viewBox="0 0 16 16" aria-hidden="true"><circle cx="8" cy="8" r="8" fill="var(--icon)"/><path d="M5.2 4.2l1.4-.3.9 2-1 .8a5 5 0 0 0 2.7 2.7l.8-1 2 .9-.3 1.4c-3.6.5-7-2.9-6.5-6.5z" fill="var(--bg)"/></svg>
      <svg viewBox="0 0 16 16" aria-hidden="true"><circle cx="8" cy="8" r="8" fill="var(--icon)"/><g fill="none" stroke="var(--bg)" stroke-width="1"><circle cx="8" cy="8" r="4.8"/><ellipse cx="8" cy="8" rx="2" ry="4.8"/><path d="M3.2 8h9.6M8 3.2v9.6"/></g></svg>
    </div>
    <p class="contact__lines">744-312-0846<br>www.bellamonte.com.mx</p>
  </section>

  <section class="card card--cream">
    <div class="card__frame"></div>
    <div class="brand__square"></div>
    <h1 class="brand__name">BELLAMONTE</h1>
    <svg class="contact__pin" viewBox="0 0 18 27" aria-hidden="true"><path d="M9 1a8 8 0 0 0-8 8c0 6 8 13 8 13s8-7 8-13a8 8 0 0 0-8-8z" fill="var(--icon)"/><circle cx="9" cy="8.5" r="3" fill="var(--bg)"/><rect x="2" y="24.5" width="14" height="2" fill="var(--icon)"/></svg>
    <address class="contact__address">Camelia 415<br>Playa Azul,<br>Guerrero CP 40880</address>
    <div class="contact__icons">
      <svg viewBox="0 0 16 16" aria-hidden="true"><circle cx="8" cy="8" r="8" fill="var(--icon)"/><path d="M5.2 4.2l1.4-.3.9 2-1 .8a5 5 0 0 0 2.7 2.7l.8-1 2 .9-.3 1.4c-3.6.5-7-2.9-6.5-6.5z" fill="var(--bg)"/></svg>
      <svg viewBox="0 0 16 16" aria-hidden="true"><circle cx="8" cy="8" r="8" fill="var(--icon)"/><g fill="none" stroke="var(--bg)" stroke-width="1"><circle cx="8" cy="8" r="4.8"/><ellipse cx="8" cy="8" rx="2" ry="4.8"/><path d="M3.2 8h9.6M8 3.2v9.6"/></g></svg>
    </div>
    <p class="contact__lines">744-312-0846<br>www.bellamonte.com.mx</p>
  </section>

</main>
</body>
</html>
```